Harbourline Refrigeration business card design

We would like a new design for our business card as we have a new logo.
We need generic business card to give our customers with our office details - with the option of making it individualized for each manager

Target Market(s)

Companies and homeowners

Industry/Entity Type

Air Conditioning

Contact Information for Business Card

We are not sure if we want single or double sided it will depend on the design we choose

Colors
33a6d7
0255a3

Requirements
Must have
• Logo
• phone: (08) 8721 5940
• email: harbourserve@tealnet.example
• website: www.harbourlinerefrigeration.example
• AU61420
• BLD472913
Nice to have
• Address - Shed 5/284 Tallis Rd, Kestrel Flats SA 5790

```html
<!DOCTYPE html>
<html lang="en">
<head>
<meta charset="utf-8">
<title>Harbourline Refrigeration – Business Card</title>
<link href="https://fonts.googleapis.com/css2?family=Roboto:wght@400;500;700&family=Roboto+Condensed:wght@400;700&display=swap" rel="stylesheet">
<style>
  :root {
    --brand-navy: #0a4a8f;
    --brand-blue: #0255a3;
    --brand-sky: #33a6d7;
    --ink: #3d4450;
    --paper: #ffffff;
    --stage: #e9ebee;
  }
  * { box-sizing: border-box; margin: 0; padding: 0; }
  html, body { width: 1200px; height: 911px; overflow: hidden; }
  body {
    background: var(--stage);
    font-family: "Roboto", Arial, sans-serif;
    position: relative;
  }
  .card {
    position: absolute;
    left: 280px;
    width: 640px;
    height: 366px;
    box-shadow: 0 4px 14px rgba(0,0,0,0.12);
    overflow: hidden;
  }
  .card--front { top: 64px; background: var(--paper); }
  .card--back  { top: 478px; background: var(--brand-blue); }

  /* Front */
  .name-band {
    position: absolute;
    top: 22px;
    right: 0;
    width: 300px;
    height: 72px;
    background: var(--brand-blue);
    color: var(--paper);
    font-family: "Roboto Condensed", Arial, sans-serif;
    padding: 12px 0 0 24px;
  }
  .name-band__name { font-weight: 700; font-size: 25px; letter-spacing: 0.5px; line-height: 1.05; }
  .name-band__role { font-size: 18px; letter-spacing: 0.5px; margin-top: 2px; }
  .name-band__dot {
    position: absolute;
    top: 40px;
    right: 316px;
    width: 38px;
    height: 38px;
    border-radius: 50%;
    background: var(--brand-sky);
  }

  .brand {
    position: absolute;
    left: 46px;
    top: 114px;
    display: flex;
    align-items: center;
    gap: 12px;
  }
  .brand__dot {
    width: 26px; height: 26px; border-radius: 50%;
    background: var(--brand-sky);
  }
  .brand__name {
    font-family: "Roboto", Arial, sans-serif;
    font-weight: 400;
    font-size: 28px;
    color: var(--brand-navy);
  }

  .contact {
    position: absolute;
    left: 52px;
    top: 190px;
    list-style: none;
    font-size: 14px;
    line-height: 19px;
    color: var(--ink);
  }
  .contact__item { display: flex; align-items: flex-start; gap: 12px; margin-bottom: 8px; }
  .contact__item--group { margin-bottom: 14px; }
  .contact__icon { width: 14px; height: 14px; margin-top: 2px; flex: none; fill: var(--brand-navy); }

  /* Back */
  .back-web {
    position: absolute;
    left: 34px;
    top: 30px;
    font-size: 13px;
    letter-spacing: 3.2px;
    color: var(--paper);
  }
  .back-brand {
    position: absolute;
    left: 0; right: 0; top: 162px;
    display: flex;
    justify-content: center;
    align-items: center;
    gap: 14px;
  }
  .back-brand__dot { width: 32px; height: 32px; border-radius: 50%; background: var(--brand-sky); }
  .back-brand__name {
    font-weight: 400;
    font-size: 32px;
    color: var(--paper);
  }
</style>
</head>
<body>

<section class="card card--front">
  <span class="name-band__dot"></span>
  <div class="name-band">
    <div class="name-band__name">DANIEL CARVER</div>
    <div class="name-band__role">CEO/FOUNDER</div>
  </div>

  <div class="brand">
    <span class="brand__dot"></span>
    <span class="brand__name">Harbourline Refrigeration</span>
  </div>

  <ul class="contact">
    <li class="contact__item contact__item--group">
      <svg class="contact__icon" viewBox="0 0 24 24"><path d="M12 2a7 7 0 0 0-7 7c0 5 7 13 7 13s7-8 7-13a7 7 0 0 0-7-7zm0 9.5A2.5 2.5 0 1 1 12 6.5a2.5 2.5 0 0 1 0 5z"/></svg>
      <span>Shed 5/284 Tallis Rd<br>Kestrel Flats SA 5790<br>AU61420 | BLD472913</span>
    </li>
    <li class="contact__item">
      <svg class="contact__icon" viewBox="0 0 24 24"><path d="M6.6 10.8a15.1 15.1 0 0 0 6.6 6.6l2.2-2.2a1 1 0 0 1 1-.25 11.4 11.4 0 0 0 3.6.57 1 1 0 0 1 1 1V20a1 1 0 0 1-1 1A17 17 0 0 1 3 4a1 1 0 0 1 1-1h3.5a1 1 0 0 1 1 1c0 1.25.2 2.45.57 3.57a1 1 0 0 1-.25 1z"/></svg>
      <span>(08) 8721 5940</span>
    </li>
    <li class="contact__item">
      <svg class="contact__icon" viewBox="0 0 24 24"><path d="M3 5h18v14H3z M3 5l9 7 9-7" fill="none" stroke="#0a4a8f" stroke-width="2.4"/></svg>
      <span>harbourserve@tealnet.example</span>
    </li>
    <li class="contact__item">
      <svg class="contact__icon" viewBox="0 0 24 24"><circle cx="12" cy="12" r="9" fill="none" stroke="#0a4a8f" stroke-width="2.4"/><path d="M3 12h18M12 3c3 3 3 15 0 18M12 3c-3 3-3 15 0 18" fill="none" stroke="#0a4a8f" stroke-width="1.8"/></svg>
      <span>www.harbourlinerefrigeration.example</span>
    </li>
  </ul>
</section>

<section class="card card--back">
  <div class="back-web">www.harbourlinerefrigeration.example</div>
  <div class="back-brand">
    <span class="back-brand__dot"></span>
    <span class="back-brand__name">Harbourline Refrigeration</span>
  </div>
</section>

</body>
</html>
```